Artsy stationary pack for unique new business
It's time to get Creative - Great Portfolio Project!
Artsy stationary pack for unique new business - Entertainment
Creative Brief
Professional
Ivo
President
no street address on business card, but rest of stationary: 4725 Pine Hollow Lane Louisville, KY 40299
1-855-QR TIMBO
Ivo@TwirlMarkHall.example
TwirlMarkHall.example
creative brief for stationary Brand new ballroom and latin dance website needs artsy and unique stationary for chic, upscale clientele. Items needed: business cards, fax cover sheet, letterhead, envelopes, presentation folders, cd cases, cd labels, email signature, the works! Two designs for business cards: Card design needs to be very artistic and chic. Two-sided design for both cards. The FRONT on both of the cards will probably be the same. FRONT DESIGN: The card FRONT will either be black, or a dark gray and black mottled pattern (something non-descript, no wood floor designs). The logo will be in full color, spot uv, starting from the left side of the card and spreading to the right (the logo has a horizontal design). There may be a soft glow under the logo to break it from the background. or maybe not Maybe the upper right corner and lower left corner are rounded, with the upper left corner and lower right corner are left squared. Or maybe just the upper right hand corner is rounded. may include tag line “Step In; Glide On”. or maybe not BACK DESIGN FOR CARD 1: The card BACK will either be black, or a dark gray and black mottled pattern (something non-descript, no wood floor designs). The name on the card, and the title (example - Ivo, (no last name), President) will both be in silver or gold foil. The other contact information (website, phone number, etc) will be in black, with spot uv. SEE ATTACHED CARD SAMPLES CONTACT INFORMATION FOR BUSINESS CARD 1 (Contact information needs to be in an editable PSD Layer so that it can be changed later as necessary): Ivo President ivo@twirlmarkhall.example 1-855-QR TIMBO TwirlMarkHall.example facebook.com/twirlmarkhall twitter.com/TwirlMarkChirp No Mailing Address I like the idea of having very small icons in front of address, website, fb, and so on BACK DESIGN FOR CARD 2: The card BACK will either be black, or a dark gray and black mottled pattern (something non-descript, no wood floor designs) or could be a COLOR to compliment logo on front. The font can match the colors in the logo on the front, or designers choice. These cards are reminders for new customers when they create a new online account. There will be two fields that will be left blank and filled in on-site: Login: Password: These fields should have a light background and be large enough, so they can be easily written on. Other contact information for the company needs to fit around these two fields. Maybe contact information is at angles, or curving around the edges of the card. contact same as card 1 SEE ATTACHED CARD SAMPLES CONTACT INFORMATION FOR LETTERHEAD, ENVELOPES, FAX, ETC: TwirlMarkHall.example 4725 Pine Hollow Lane Louisville, Kentucky 40299 1-855-QR TIMBO I like the idea of having very small icons in front of address, website, fb, and so on The color scene of the whole thing is black, dark, yellow, gold, silver. The picture from the website gives you an idea. The rest of the stationary -- creative, not boring, artistic, classy, chic, the fancier the better.
see first part

```html
<!DOCTYPE html>
<html lang="en">
<head>
<meta charset="utf-8">
<title>TwirlMark Hall – Business Card</title>
<link href="https://fonts.googleapis.com/css2?family=Cinzel:wght@400;700&display=swap" rel="stylesheet">
<style>
  :root {
    --stage: #2b2622;
    --card-black: #0b0b0c;
    --card-edge: #1d1d20;
    --silver: #d9d9dc;
    --silver-dim: #a9a9ae;
    --blue: #2f6fb0;
    --blue-deep: #163a66;
  }
  * { box-sizing: border-box; margin: 0; padding: 0; }
  html, body {
    width: 1200px; height: 468px; overflow: hidden;
    background: var(--stage);
    font-family: "Cinzel", serif;
  }
  .stage {
    position: relative; width: 1200px; height: 468px;
    display: flex; justify-content: center; align-items: center; gap: 26px;
  }
  .card {
    position: relative; width: 562px; height: 400px;
    border-radius: 26px; overflow: hidden;
    background: radial-gradient(ellipse at 40% 30%, #1c1c1f 0%, var(--card-black) 70%);
    box-shadow: 0 0 0 1px var(--card-edge);
  }
  /* Brand name set in plain text */
  .brand-name {
    font-weight: 400; color: var(--silver); letter-spacing: 1px; white-space: nowrap;
  }
  /* Back card */
  .back-brand {
    position: absolute; left: 36px; top: 46px; font-size: 26px;
  }
  .person { position: absolute; left: 40px; top: 150px; width: 250px; text-align: center; }
  .person-name { font-size: 38px; color: var(--silver); letter-spacing: 2px; }
  .person-title { font-size: 21px; color: var(--silver); margin-top: 2px; letter-spacing: 1px; }
  .address { margin-top: 12px; font-size: 11.5px; line-height: 1.5; color: var(--silver-dim); }
  .divider {
    position: absolute; left: 296px; top: 170px; width: 1px; height: 120px;
    background: var(--silver-dim); opacity: .6;
  }
  .contact {
    position: absolute; left: 312px; top: 180px;
    font-size: 13px; line-height: 1.9; color: var(--silver);
  }
  .website {
    position: absolute; left: 312px; top: 272px;
    font-size: 13.5px; color: var(--silver); letter-spacing: .5px;
  }
  .swoosh { position: absolute; left: 0; bottom: 0; width: 562px; height: 110px; }
  /* Front card */
  .halftone {
    position: absolute; right: 0; top: 0; width: 240px; height: 240px;
    background: radial-gradient(circle at 100% 0%, rgba(150,150,160,.35) 0%, rgba(80,80,90,.12) 45%, transparent 72%);
  }
  .front-brand {
    position: absolute; left: 0; right: 0; top: 176px;
    text-align: center; font-size: 40px;
  }
</style>
</head>
<body>
<main class="stage">
  <section class="card card-back" aria-label="Card back with contact details">
    <p class="brand-name back-brand">TwirlMark Hall</p>
    <div class="person">
      <p class="person-name">Ivo</p>
      <p class="person-title">President</p>
      <p class="address">No street address on business card<br>but rest of stationary:<br>4725 Pine Hollow Lane<br>Louisville, KY 40299</p>
    </div>
    <span class="divider"></span>
    <div class="contact">
      <p>P: 1-855-QR TIMBO</p>
      <p>E: Ivo@TwirlMarkHall.example</p>
    </div>
    <p class="website">TwirlMarkHall.example</p>
    <svg class="swoosh" viewBox="0 0 562 110" preserveAspectRatio="none" aria-hidden="true">
      <defs>
        <linearGradient id="blueBand" x1="0" x2="1" y1="0" y2="0">
          <stop offset="0" stop-color="#0d2440"/>
          <stop offset=".6" stop-color="#2f6fb0"/>
          <stop offset="1" stop-color="#5a97d6"/>
        </linearGradient>
        <linearGradient id="goldBand" x1="0" x2="1" y1="0" y2="0">
          <stop offset="0" stop-color="#9c6f1c"/>
          <stop offset=".5" stop-color="#e8bd55"/>
          <stop offset="1" stop-color="#9c6f1c"/>
        </linearGradient>
      </defs>
      <path d="M0 70 C160 30 330 95 562 40 L562 110 L0 110 Z" fill="url(#blueBand)"/>
      <path d="M0 62 C160 20 330 88 562 30 L562 38 C330 96 160 34 0 70 Z" fill="url(#goldBand)"/>
    </svg>
  </section>

  <section class="card card-front" aria-label="Card front with brand name">
    <div class="halftone" role="img" aria-label="Soft dotted halftone texture in the corner"></div>
    <p class="brand-name front-brand">TwirlMark Hall</p>
  </section>
</main>
</body>
</html>
```